Treatment Info-Graphic Poster

22 x 28 poster. We need a design for a poster to hang in our treatment rooms that quickly compares different treatments we offer and sets expectations for the patient. Attached is something I very quickly created on Excel, but we would like one that matches our company colors and looks much more polished. I have attached a info-graphic we have had designed prior for reference.

Target Market(s)

Osteoarthritis of the knee patients treatment comparison info graphic for poster

Font styles to use
Serif

Colors
85cae6
f78f20

Requirements
Must have
• Branded treatment comparison table
Nice to have
• Treatment graphics

```html
<!DOCTYPE html>
<html lang="en">
<head>
<meta charset="utf-8">
<title>Knee OA Treatment Comparison</title>
<link href="https://fonts.googleapis.com/css2?family=Montserrat:wght@400;600;700;800&family=Merriweather:wght@400&display=swap" rel="stylesheet">
<style>
:root{
  --page:#e3e4e6;
  --teal-deep:#4b7b86;
  --teal:#6aaebf;
  --teal-light:#85cae6;
  --tick-teal:#6aaab9;
  --orange:#f78f20;
  --orange-deep:#d9701a;
  --slate:#525254;
  --slate-dark:#444446;
  --cell:#f7f7f7;
  --cell-edge:#e4e4e4;
  --ink:#5a5a5c;
  --white:#ffffff;
}
*{box-sizing:border-box;margin:0;padding:0}
html,body{width:1200px;height:963px;overflow:hidden;background:var(--page);font-family:"Montserrat",sans-serif}
.poster{position:absolute;left:86px;top:74px;width:1028px;height:808px;background:var(--white);overflow:hidden}
.poster-backdrop{position:absolute;left:0;top:0;width:1028px;height:683px;background:linear-gradient(160deg,#5a8d98 0%,var(--teal-deep) 55%,#6b9aa3 100%)}
.knee-art{position:absolute;left:0;top:0;width:110px;height:140px;background:radial-gradient(ellipse at 40% 40%,rgba(240,225,215,.45),rgba(240,225,215,0) 70%)}
.title{position:absolute;left:0;width:100%;top:28px;text-align:center;color:var(--white);font-weight:800;font-size:46px;letter-spacing:.5px}
.col{position:absolute;top:108px;width:172px;height:602px;border-radius:14px;overflow:hidden;background:var(--cell);box-shadow:0 2px 4px rgba(0,0,0,.2)}
.col-head{height:118px;padding:8px 12px 0;color:var(--white);position:relative}
.col-head.teal{background:linear-gradient(180deg,#72b4c4,#4f95a6)}
.col-head.orange{background:linear-gradient(180deg,#f79a2e,var(--orange-deep))}
.col-name{font-weight:700;font-size:15.5px;line-height:23px}
.col-icon{position:absolute;right:10px;top:30px}
.grade-label{position:absolute;right:11px;top:70px;font-size:6px}
.grade-list{position:absolute;left:12px;right:16px;top:80px;font-size:6px;line-height:8.3px}
.grade-list div{display:flex;justify-content:space-between}
.grade-list span:last-child{width:28px}
.cell{height:44px;border-top:1px solid var(--cell-edge);background:linear-gradient(180deg,#fff,#ececec);display:flex;align-items:center;justify-content:center}
.label-col{position:absolute;left:35px;top:108px;width:242px;height:602px;border-radius:14px;overflow:hidden;background:var(--slate);box-shadow:0 2px 4px rgba(0,0,0,.25)}
.label-head{height:118px;background:linear-gradient(180deg,#76b6c6,#4f93a4);display:flex;align-items:center;justify-content:center}
.brand{width:134px;height:86px;border:4px solid var(--white);border-radius:10px;background:var(--teal);display:flex;flex-direction:column;align-items:center;justify-content:center;gap:6px;color:var(--white);font-family:"Merriweather",serif}
.brand-name{font-size:18px}
.brand-sub{font-size:10px}
.label{height:44px;border-top:2px solid var(--teal-deep);background:linear-gradient(180deg,#5b5b5d,var(--slate-dark));color:var(--white);font-weight:700;font-size:12.2px;line-height:16px;padding-left:21px;display:flex;align-items:center}
.label.indent{padding-left:59px}
.average-band{position:absolute;left:0;top:382px;width:48px;height:132px;background:linear-gradient(180deg,var(--orange-deep),var(--orange));color:var(--white);font-weight:700;font-size:12px;display:flex;align-items:center;justify-content:center}
.average-band span{transform:rotate(-90deg);white-space:nowrap}
.disclaimer{position:absolute;left:0;width:100%;top:724px;text-align:center;color:var(--ink);font-weight:600;font-size:13px;line-height:20px}
.stethoscope-art{position:absolute;left:935px;top:725px;width:70px;height:72px;border-radius:50%;background:radial-gradient(circle,rgba(133,202,230,.25),rgba(133,202,230,0) 70%)}
.site{position:absolute;left:365px;top:775px;width:298px;height:33px;border-radius:22px 22px 0 0;background:linear-gradient(180deg,var(--orange-deep),var(--orange));color:var(--white);font-weight:700;font-size:20px;text-align:center;line-height:34px}
</style>
</head>
<body>
<svg width="0" height="0" style="position:absolute">
  <defs>
    <symbol id="tick" viewBox="0 0 40 27"><path d="M2 13 L14 24 L38 2" fill="none" stroke="currentColor" stroke-width="4.5"/></symbol>
    <symbol id="syringe" viewBox="0 0 24 24"><path d="M21 3 L15 9 M18 2 L22 6 M16 5 L6 15 L9 18 L19 8 Z M6 15 L2 22 M9 11 L11 13 M11 9 L13 11" fill="none" stroke="#fff" stroke-width="1.8"/></symbol>
  </defs>
</svg>
<main class="poster">
  <div class="poster-backdrop"></div>
  <div class="knee-art" role="img" aria-label="Soft illustration of a knee joint"></div>
  <h1 class="title">KNEE OA TREATMENT COMPARISON</h1>

  <section class="label-col">
    <div class="label-head">
      <div class="brand"><span class="brand-name">Stridewell</span><span class="brand-sub">Knee Clinic</span></div>
    </div>
    <div class="label">Cushion &amp; Lubricate</div>
    <div class="label">Decrease Inflammation</div>
    <div class="label">Stimulates Synovial<br>Production of HA</div>
    <div class="label">Healing Properties</div>
    <div class="label">Reparative Properties</div>
    <div class="label">Potential Cartilage<br>Regeneration</div>
    <div class="label indent">Benefits Last 4-6 Months</div>
    <div class="label indent">Benefits Last 6-12 Months</div>
    <div class="label indent">Benefits Last 18+ Months</div>
    <div class="label">Corrects Biomechanics<br>&amp; Stabilizes Joint</div>
    <div class="label">Covered by MOST Insurance</div>
    <div class="average-band"><span>On Average,</span></div>
  </section>

  <section class="col" style="left:285px;color:var(--tick-teal)">
    <div class="col-head teal">
      <div class="col-name">Hyaluronic Acid<br>(HA)</div>
      <svg class="col-icon" width="24" height="24"><use href="#syringe"/></svg>
      <div class="grade-label">OA Grade</div>
      <div class="grade-list">
        <div><span>Single Injection (Lumagel)</span><span>1,2,3,4</span></div>
        <div><span>Single Injection (Viscora)</span><span>1,2,3,4</span></div>
        <div><span>3 Part Injection Series (Flexicel)</span><span>1,2,3,4</span></div>
        <div><span>3/4 Part Injection Series (Synovra)</span><span>1,2,3,4</span></div>
      </div>
    </div>
    <div class="cell"><svg width="38" height="26"><use href="#tick"/></svg></div>
    <div class="cell"><svg width="38" height="26"><use href="#tick"/></svg></div>
    <div class="cell"><svg width="38" height="26"><use href="#tick"/></svg></div>
    <div class="cell"></div><div class="cell"></div><div class="cell"></div>
    <div class="cell"><svg width="38" height="26"><use href="#tick"/></svg></div>
    <div class="cell"></div><div class="cell"></div><div class="cell"></div>
    <div class="cell"><svg width="38" height="26"><use href="#tick"/></svg></div>
  </section>

  <section class="col" style="left:464px;color:var(--orange)">
    <div class="col-head orange">
      <div class="col-name">Platelet Rich<br>Plasma (PRP)</div>
      <svg class="col-icon" width="24" height="24"><use href="#syringe"/></svg>
      <div class="grade-label">OA Grade</div>
      <div class="grade-list">
        <div><span>Single Injection (Plasmacell)</span><span>1, 2</span></div>
        <div><span>2 Part Injection Series</span><span>3, 4</span></div>
      </div>
    </div>
    <div class="cell"><svg width="38" height="26"><use href="#tick"/></svg></div>
    <div class="cell"><svg width="38" height="26"><use href="#tick"/></svg></div>
    <div class="cell"><svg width="38" height="26"><use href="#tick"/></svg></div>
    <div class="cell"><svg width="38" height="26"><use href="#tick"/></svg></div>
    <div class="cell"></div><div class="cell"></div><div class="cell"></div>
    <div class="cell"><svg width="38" height="26"><use href="#tick"/></svg></div>
    <div class="cell"></div><div class="cell"></div><div class="cell"></div>
  </section>

  <section class="col" style="left:642px;color:var(--tick-teal)">
    <div class="col-head teal">
      <div class="col-name">Stem Cell Therapy<br>&amp; PRP</div>
      <svg class="col-icon" width="24" height="24"><use href="#syringe"/></svg>
      <div class="grade-label">OA Grade</div>
      <div class="grade-list">
        <div><span>Single Injection</span><span>1,2,3,4</span></div>
      </div>
    </div>
    <div class="cell"><svg width="38" height="26"><use href="#tick"/></svg></div>
    <div class="cell"><svg width="38" height="26"><use href="#tick"/></svg></div>
    <div class="cell"><svg width="38" height="26"><use href="#tick"/></svg></div>
    <div class="cell"><svg width="38" height="26"><use href="#tick"/></svg></div>
    <div class="cell"><svg width="38" height="26"><use href="#tick"/></svg></div>
    <div class="cell"><svg width="38" height="26"><use href="#tick"/></svg></div>
    <div class="cell"></div><div class="cell"></div>
    <div class="cell"><svg width="38" height="26"><use href="#tick"/></svg></div>
    <div class="cell"></div><div class="cell"></div>
  </section>

  <section class="col" style="left:821px;color:var(--orange)">
    <div class="col-head orange">
      <div class="col-name">Knee Brace(s)</div>
      <div class="grade-label">OA Grade</div>
      <div class="grade-list">
        <div><span>Unloader 2</span><span>1,2,3,4</span></div>
        <div><span>Patellar Stabilization</span><span>1,2,3,4</span></div>
        <div><span>Meniscus Injuries</span><span>1,2,3,4</span></div>
      </div>
    </div>
    <div class="cell"></div><div class="cell"></div><div class="cell"></div><div class="cell"></div>
    <div class="cell"></div><div class="cell"></div><div class="cell"></div><div class="cell"></div>
    <div class="cell"><svg width="38" height="26"><use href="#tick"/></svg></div>
    <div class="cell"><svg width="38" height="26"><use href="#tick"/></svg></div>
    <div class="cell"><svg width="38" height="26"><use href="#tick"/></svg></div>
  </section>

  <p class="disclaimer">Treatment outcomes vary by individual. Treatment benefits and length of efficacy are not guaranteed. In some cases, patient’s<br>do not respond to treatment. Multiple treatments may be recommended or necessary for the best outcomes.</p>
  <div class="stethoscope-art" role="img" aria-label="Faint stethoscope illustration"></div>
  <div class="site">www.stridewellknees.com</div>
</main>
</body>
</html>
```